We need a business card design for our website rvkventures.com. The Star Headline is rvkventures.com, in large lettering.We sell fashion rings of titanium, mirror pollished stainless steel, and related jewelry. Basically quality products competing with the high expense of gold.We have to portray honesty and trust, because thats who I am. I know marketing, but I am weak on colors and layout. 3D Gold curved edge letters are ok. No green and yellow.Black,Red,Purple and White in small amounts.No fancy Lettering.
No Rainbows in printing.
Our goal is selling our products online globally

Kind Regards Corwin Albury

Fashion

rvkventures.com
known for our ideal fit rings
email.corwinalburyptyltd@fernmail com

```html
<!DOCTYPE html>
<html lang="en">
<head>
<meta charset="utf-8">
<title>rvkventures.com business card</title>
<link href="https://fonts.googleapis.com/css2?family=Arimo:wght@400&display=swap" rel="stylesheet">
<style>
  :root {
    --page: #ffffff;
    --card-edge: #c9c9c9;
    --card-light: #fbfbfb;
    --card-mid: #e4e5e6;
    --card-dark: #c6c8ca;
    --gold: #b3a06b;
    --gold-rule: #c9bb8e;
    --band: #4b504b;
    --ink: #111111;
    --white: #ffffff;
  }
  * { margin: 0; padding: 0; box-sizing: border-box; }
  html, body {
    width: 1200px;
    height: 742px;
    overflow: hidden;
    background: var(--page);
    font-family: "Arimo", Arial, sans-serif;
  }
  .card {
    position: absolute;
    left: 17px;
    top: 18px;
    width: 1166px;
    height: 706px;
    border-radius: 48px;
    border: 2px solid var(--card-edge);
    overflow: hidden;
    background: radial-gradient(ellipse 70% 80% at 50% 38%, var(--card-light) 0%, var(--card-mid) 60%, var(--card-dark) 100%);
  }
  .product-photo {
    position: absolute;
    left: 470px;
    top: 160px;
    width: 300px;
    height: 300px;
    border-radius: 50%;
    background: radial-gradient(circle at 50% 50%, #ffffff 0%, #f3f3f3 35%, #d2d4d6 55%, rgba(228,229,230,0) 72%);
  }
  .brand-name {
    position: absolute;
    left: 0;
    width: 100%;
    top: 446px;
    text-align: center;
    font-size: 68px;
    color: var(--gold);
    letter-spacing: 0.5px;
  }
  .tagline {
    position: absolute;
    left: 0;
    width: 100%;
    top: 522px;
    text-align: center;
    font-size: 26px;
    color: var(--ink);
  }
  .gold-rule {
    position: absolute;
    left: 0;
    width: 100%;
    top: 598px;
    height: 6px;
    background: var(--gold-rule);
  }
  .contact-band {
    position: absolute;
    left: 0;
    width: 100%;
    top: 610px;
    bottom: 0;
    background: var(--band);
    display: flex;
    align-items: center;
    justify-content: center;
  }
  .email {
    color: var(--white);
    font-size: 28px;
    margin-top: -6px;
  }
</style>
</head>
<body>
  <div class="card">
    <div class="product-photo" role="img" aria-label="Photo of a pair of polished titanium wedding bands with gold inlay lines"></div>
    <h1 class="brand-name" style="font-weight:400">rvkventures.com</h1>
    <p class="tagline">Known for our ideal fit rings</p>
    <div class="gold-rule"></div>
    <div class="contact-band">
      <p class="email">email.corwinalburyptyltd@fernmail com</p>
    </div>
  </div>
</body>
</html>
```